Personal Injury Law Firm Marketing Postcards

Looking for 4 different high quality graphic postcards (print on both sides of 4"x6" postcard to market a Personal Injury Lawyer (Walter Gimsby). These will be placed on cars and in stores on stands. My photo and/or stock images.... We are targeting People who have been injured in automobile accidents, motorcycle accidents, slip and fall (wet/greasy floors indoors in supermarkets, restaurants, etc., snow and ice outdoors on sidewalks) trip and fall cases on dangerous staircases. indoor/outdoor, dog bite injuries. ( I like the use of stock images of these type of injury causing accidents. You can use following language "Serving People Injured in NY & NJ" . Millions of Dollars Recovered, Free Consultation and No Fee Unless We Recover Money! Phone number to be displayed (555) 418-3062 "call or text" Available 24 hours a day 7 days per week. May also want to mention that we can take over your case from another lawyer if you are not satisfied with your current attorney. There should be a small space in corner which has a space for my marketing person to handwrite in their reference code.

Target Market(s)

18-75 years old - densely populated major city

Industry/Entity Type

Legal

Font styles to use
Other font styles liked:
• Please use logo style that I uploaded.. Please do not just cut parts of my website out and use them. Do not use LOGO from my website

Colors
0054AA
0677BA
7BADD7
CADEEF
E8F1F8
00AB8E
00BBA5
67D7C9
C6EFE9
E9F9F6

Requirements
Must have
• Professional Appearance

```html
<!DOCTYPE html>
<html lang="en">
<head>
<meta charset="utf-8">
<title>Walter Gimsby Postcard – Front and Back</title>
<link rel="stylesheet" href="https://fonts.googleapis.com/css2?family=Playfair+Display:wght@400;700&family=Roboto:wght@300;400;500&family=Roboto+Condensed:wght@400&display=swap">
<style>
:root{
  --board:#666666;
  --paper:#ffffff;
  --panel:#e6e6e6;
  --panel-soft:#f4f4f4;
  --ink:#1e1e1e;
  --ink-soft:#5a5a5a;
  --icon:#6f6f6f;
  --dark:#262626;
  --dark-2:#3a3a3a;
  --gold:#c9a45a;
  --gold-light:#eedfa8;
  --gold-deep:#a9823a;
  --white:#ffffff;
}
*{margin:0;padding:0;box-sizing:border-box}
html,body{width:1200px;height:1200px;overflow:hidden;background:var(--board)}
.board{position:relative;width:1200px;height:1200px;background:var(--board)}
.side-label{position:absolute;font-family:"Playfair Display",serif;font-weight:400;font-size:34px;color:var(--white);letter-spacing:1px}
.side-label--front{left:866px;top:306px}
.side-label--back{left:182px;top:862px}
.card{position:absolute;overflow:hidden;background:var(--paper)}
.card--front{left:92px;top:66px;width:743px;height:502px}
.card--back{left:327px;top:623px;width:747px;height:505px}
.card svg.shapes{position:absolute;left:0;top:0}
.abs{position:absolute}
.brand-name{font-family:"Roboto",sans-serif;font-weight:500;color:var(--gold);font-size:11.5px;line-height:11.5px;text-align:center;text-transform:uppercase;letter-spacing:-.3px}
.headline{font-family:"Playfair Display",serif;font-weight:400;color:var(--ink);font-size:41px;line-height:43px;letter-spacing:-1px;left:158px;top:22px}
.practice-title{font-family:"Playfair Display",serif;font-weight:700;color:var(--ink);font-size:20px;left:57px;top:172px;letter-spacing:.3px}
.area{position:absolute;width:96px;text-align:center;font-family:"Roboto Condensed",sans-serif;font-size:9.6px;line-height:12px;color:var(--ink);text-transform:uppercase}
.area svg{display:block;margin:0 auto 4px;width:18px;height:15px}
.nameplate{left:425px;top:386px;width:136px;height:42px;background:#dcdcdc;text-align:right;padding:3px 4px 0 0}
.nameplate .name{font-family:"Playfair Display",serif;font-weight:400;font-size:18.5px;line-height:22px;color:var(--ink);letter-spacing:-.5px;white-space:nowrap}
.nameplate .role{font-family:"Playfair Display",serif;font-size:7.5px;color:var(--ink)}
.call-label{font-family:"Roboto",sans-serif;font-weight:300;color:var(--white);font-size:16px}
.call-number{font-family:"Roboto",sans-serif;font-weight:400;color:var(--white);font-size:24.5px;letter-spacing:-.4px}
.hours{font-family:"Roboto",sans-serif;font-weight:300;color:var(--white);font-size:9.8px;line-height:13px;text-transform:uppercase}
.benefit{font-family:"Roboto",sans-serif;font-size:8.8px;line-height:11.5px;color:var(--ink-soft);text-transform:uppercase}
.benefit strong{color:var(--ink);font-weight:500}
.bio-title{font-family:"Playfair Display",serif;font-weight:400;font-size:17.5px;line-height:20.5px;color:var(--ink);left:211px;top:91px;letter-spacing:-.4px}
.bio-text{font-family:"Roboto",sans-serif;font-weight:300;font-size:7.4px;line-height:9.38px;color:var(--ink-soft);text-align:justify;left:211px;top:162px;width:154px}
.stamp-box{left:650px;top:17px;width:77px;height:89px;border:1px solid #8a8a8a}
</style>
</head>
<body>
<div class="board">

  <div class="side-label side-label--front">FRONT</div>
  <div class="side-label side-label--back">BACK</div>

  <!-- FRONT SIDE -->
  <section class="card card--front">
    <svg class="shapes" width="743" height="502" viewBox="0 0 743 502">
      <defs>
        <linearGradient id="goldBar" x1="0" y1="0" x2="1" y2="0">
          <stop offset="0" stop-color="#b68d45"/><stop offset=".5" stop-color="#e9d38e"/><stop offset="1" stop-color="#c39c55"/>
        </linearGradient>
        <linearGradient id="goldFrame" x1="0" y1="1" x2="1" y2="0">
          <stop offset="0" stop-color="#b08840"/><stop offset=".5" stop-color="#f0e2ad"/><stop offset="1" stop-color="#c7a257"/>
        </linearGradient>
        <linearGradient id="sceneBase" x1="0" y1="0" x2="1" y2="1">
          <stop offset="0" stop-color="#3f5a35"/><stop offset=".3" stop-color="#6f7f82"/><stop offset=".5" stop-color="#8e9aa0"/><stop offset=".72" stop-color="#46536a"/><stop offset="1" stop-color="#20283a"/>
        </linearGradient>
        <radialGradient id="sceneLight" cx=".42" cy=".45" r=".35">
          <stop offset="0" stop-color="#b7c4c9" stop-opacity=".75"/><stop offset="1" stop-color="#b7c4c9" stop-opacity="0"/>
        </radialGradient>
        <radialGradient id="sceneShade" cx=".82" cy=".78" r=".4">
          <stop offset="0" stop-color="#1d2436" stop-opacity=".85"/><stop offset="1" stop-color="#1d2436" stop-opacity="0"/>
        </radialGradient>
        <linearGradient id="darkBand" x1="0" y1="0" x2="1" y2="0">
          <stop offset="0" stop-color="#2e2e2e"/><stop offset="1" stop-color="#1c1c1c"/>
        </linearGradient>
        <linearGradient id="faint" x1="0" y1="0" x2="0" y2="1">
          <stop offset="0" stop-color="#f2f2f2"/><stop offset="1" stop-color="#ffffff"/>
        </linearGradient>
        <clipPath id="sceneClip"><polygon points="575,72 818,315 575,558 330,315"/></clipPath>
      </defs>
      <rect class="watermark" x="600" y="20" width="143" height="200" fill="url(#faint)" role="img" aria-label="faint statue of justice and column decoration"/>
      <rect class="practice-panel" x="0" y="186" width="470" height="220" fill="var(--panel)"/>
      <polygon points="39,170 282,170 257,201 39,201" fill="url(#goldBar)"/>
      <g stroke="#b9b9b9" stroke-width=".8">
        <line x1="126" y1="215" x2="126" y2="395"/>
        <line x1="220" y1="215" x2="220" y2="395"/>
        <line x1="40" y1="270" x2="300" y2="270"/>
        <line x1="40" y1="332" x2="300" y2="332"/>
      </g>
      <polyline points="430,166 575,20 720,166" fill="none" stroke="url(#goldFrame)" stroke-width="12"/>
      <polygon points="575,44 845,315 575,586 301,315" fill="var(--dark)"/>
      <polygon points="575,68 822,315 575,562 326,315" fill="#ffffff"/>
      <g clip-path="url(#sceneClip)" role="img" aria-label="photo of a crashed car with the lawyer in a suit standing in front">
        <rect x="330" y="72" width="488" height="486" fill="url(#sceneBase)"/>
        <rect x="330" y="72" width="488" height="486" fill="url(#sceneLight)"/>
        <rect x="330" y="72" width="488" height="486" fill="url(#sceneShade)"/>
      </g>
      <rect x="0" y="406" width="480" height="6" fill="#ffffff"/>
      <polygon points="0,411 30,411 46,429 384,429 458,502 0,502" fill="url(#darkBand)"/>
      <polygon points="36,411 382,411 482,502 462,502 374,424 50,424" fill="var(--gold-light)"/>
      <polygon points="540,502 580,462 590,468 556,502" fill="var(--gold)"/>
      <circle cx="46" cy="466" r="20.5" fill="none" stroke="#ffffff" stroke-width="1.8"/>
      <path d="M34 461c0-5 6-7 12-7s12 2 12 7l-4 1-2-3h-12l-2 3zM38 464h16l2 9h-20z" fill="#ffffff"/>
      <circle cx="46" cy="468" r="3" fill="#2a2a2a"/>
    </svg>

    <div class="abs brand-name" style="left:30px;top:83px;width:100px">Law Office of<br>Walter Gimsby</div>

    <h1 class="abs headline">PERSONAL<br>INJURY LAWYER<br>NY AND NJ</h1>

    <h2 class="abs practice-title">PRACTICE AREAS</h2>

    <div class="area" style="left:25px;top:215px"><svg viewBox="0 0 18 15" aria-hidden="true"><path d="M9 1L17 14H1Z" fill="var(--icon)"/><rect x="8.2" y="5" width="1.6" height="5" fill="#e6e6e6"/><rect x="8.2" y="11" width="1.6" height="1.6" fill="#e6e6e6"/></svg>Dog Bites</div>
    <div class="area" style="left:125px;top:215px"><svg viewBox="0 0 18 15" aria-hidden="true"><rect x="2" y="5" width="14" height="9" rx="1.5" fill="var(--icon)"/><path d="M6.5 5V2.5h5V5" fill="none" stroke="var(--icon)" stroke-width="1.5"/></svg>Workplace<br>Accidents</div>
    <div class="area" style="left:216px;top:215px"><svg viewBox="0 0 18 15" aria-hidden="true"><circle cx="4" cy="10.5" r="3" fill="none" stroke="var(--icon)" stroke-width="1.5"/><circle cx="14" cy="10.5" r="3" fill="none" stroke="var(--icon)" stroke-width="1.5"/><path d="M4 10.5L8 6h4l2 4.5" fill="none" stroke="var(--icon)" stroke-width="1.6"/></svg>Motorcycle<br>Accidents</div>
    <div class="area" style="left:25px;top:277px"><svg viewBox="0 0 18 15" aria-hidden="true"><path d="M1 14V11h4V8h4V5h4V2h4v12Z" fill="var(--icon)"/></svg>Trip and Fall<br>Accidents</div>
    <div class="area" style="left:125px;top:277px"><svg viewBox="0 0 18 15" aria-hidden="true"><rect x="1" y="3" width="10" height="8" fill="var(--icon)"/><path d="M11 6h3.5l2.5 3v2h-6Z" fill="var(--icon)"/><circle cx="4.5" cy="12" r="2" fill="var(--icon)" stroke="#e6e6e6"/><circle cx="13.5" cy="12" r="2" fill="var(--icon)" stroke="#e6e6e6"/></svg>Truck<br>Accidents</div>
    <div class="area" style="left:216px;top:277px"><svg viewBox="0 0 18 15" aria-hidden="true"><rect x="1" y="3" width="2.4" height="10" fill="var(--icon)"/><rect x="5.5" y="3" width="2.4" height="10" fill="var(--icon)"/><rect x="10" y="3" width="2.4" height="10" fill="var(--icon)"/><rect x="14.5" y="3" width="2.4" height="10" fill="var(--icon)"/></svg>Pedestrian<br>Accidents</div>
    <div class="area" style="left:25px;top:338px"><svg viewBox="0 0 18 15" aria-hidden="true"><path d="M9 1v12M5 14h8M2 4h14" stroke="var(--icon)" stroke-width="1.4" fill="none"/><path d="M0.5 9l2.5-5 2.5 5Z M12.5 9l2.5-5 2.5 5Z" fill="var(--icon)"/></svg>Wrongful<br>Death Attorneys</div>
    <div class="area" style="left:125px;top:338px"><svg viewBox="0 0 18 15" aria-hidden="true"><path d="M9 1C9 1 4 7 4 9.5a5 5 0 0 0 10 0C14 7 9 1 9 1Z" fill="var(--icon)"/></svg>Slip and Fall<br>Accidents</div>
    <div class="area" style="left:216px;top:338px"><svg viewBox="0 0 18 15" aria-hidden="true"><path d="M1 11V8.5l2-1 2.5-3h6l3 3 2.5.8V11Z" fill="var(--icon)"/><circle cx="5" cy="11.5" r="2" fill="var(--icon)" stroke="#e6e6e6"/><circle cx="13" cy="11.5" r="2" fill="var(--icon)" stroke="#e6e6e6"/></svg>Car<br>Accidents</div>

    <div class="abs nameplate"><div class="name">WALTER GIMSBY</div><div class="role">ACCIDENT LAWYER</div></div>

    <div class="abs call-label" style="left:73px;top:442px">Call or Text</div>
    <div class="abs call-number" style="left:73px;top:460px">(555) 418-3062</div>
    <div class="abs hours" style="left:251px;top:457px">Available 24 hours<br>a day 7 days per week</div>
  </section>

  <!-- BACK SIDE -->
  <section class="card card--back">
    <svg class="shapes" width="747" height="505" viewBox="0 0 747 505">
      <defs>
        <linearGradient id="goldBarB" x1="0" y1="0" x2="1" y2="1">
          <stop offset="0" stop-color="#f0e2ad"/><stop offset=".5" stop-color="#d2b067"/><stop offset="1" stop-color="#b08840"/>
        </linearGradient>
        <linearGradient id="portraitFill" x1="0" y1="0" x2="1" y2="1">
          <stop offset="0" stop-color="#4a4a4a"/><stop offset=".55" stop-color="#3c4256"/><stop offset="1" stop-color="#252b3c"/>
        </linearGradient>
        <radialGradient id="portraitLight" cx=".55" cy=".3" r=".3">
          <stop offset="0" stop-color="#9a7f6c" stop-opacity=".6"/><stop offset="1" stop-color="#9a7f6c" stop-opacity="0"/>
        </radialGradient>
        <linearGradient id="handsPhoto" x1="0" y1="0" x2="1" y2="1">
          <stop offset="0" stop-color="#e2dfdb"/><stop offset=".35" stop-color="#d8c0aa"/><stop offset=".6" stop-color="#c59f86"/><stop offset="1" stop-color="#6f7378"/>
        </linearGradient>
        <linearGradient id="faintB" x1="0" y1="0" x2="0" y2="1">
          <stop offset="0" stop-color="#ffffff"/><stop offset=".5" stop-color="#f5f5f5"/><stop offset="1" stop-color="#fbfbfb"/>
        </linearGradient>
      </defs>
      <rect class="text-panel" x="0" y="0" width="390" height="420" fill="var(--panel-soft)"/>
      <rect class="watermark" x="400" y="190" width="347" height="225" fill="url(#faintB)" role="img" aria-label="faint statue of justice and column decoration"/>
      <polyline points="197,0 259,63 321,0" fill="none" stroke="#cfcfcf" stroke-width="1"/>
      <polygon points="166,0 182,0 254,70 236,70" fill="url(#goldBarB)"/>
      <g fill="none" stroke="var(--gold)" stroke-width="1.1">
        <polygon points="31,30 37,34 37,41 31,45 25,41 25,34"/>
        <polyline points="28,37.5 30.5,40 34.5,35"/>
        <polygon points="31,64 37,68 37,75 31,79 25,75 25,68"/>
        <polyline points="28,71.5 30.5,74 34.5,69"/>
      </g>
      <polygon points="0,160 170,325 0,490" fill="var(--dark-2)"/>
      <polygon points="0,218 25,194 155,325 0,470" fill="url(#handsPhoto)" role="img" aria-label="photo of hands wrapping a bandage on an injured wrist"/>
      <polyline points="0,210 39,168 185,310" fill="none" stroke="url(#goldBarB)" stroke-width="9"/>
      <g role="img" aria-label="portrait of the lawyer in a suit">
        <polygon points="133,101 198,167 133,237 60,167" fill="url(#portraitFill)"/>
        <polygon points="133,101 198,167 133,237 60,167" fill="url(#portraitLight)"/>
      </g>
      <polygon points="192,188 200,196 140,258 132,250" fill="var(--gold)"/>
      <rect x="160" y="345" width="38" height="5" fill="#bdbdbd" role="img" aria-label="award badge"/>
      <rect x="162" y="354" width="36" height="5" fill="#bdbdbd" role="img" aria-label="rating badge"/>
      <rect x="162" y="364" width="34" height="30" fill="#2c4f8c" role="img" aria-label="client choice award badge"/>
      <polygon points="20,505 95,436 429,436 447,419 747,419 747,505" fill="var(--dark)"/>
      <polygon points="70,416 441,416 425,431 86,431" fill="var(--gold-light)"/>
      <polygon points="0,488 70,420 86,431 12,505 0,505" fill="var(--gold)"/>
      <circle cx="123" cy="470" r="20.5" fill="none" stroke="#ffffff" stroke-width="1.8"/>
      <path d="M111 465c0-5 6-7 12-7s12 2 12 7l-4 1-2-3h-12l-2 3zM115 468h16l2 9h-20z" fill="#ffffff"/>
      <circle cx="123" cy="472" r="3" fill="#2a2a2a"/>
    </svg>

    <div class="abs benefit" style="left:44px;top:29px">Millions of <strong>Dollars</strong><br><strong>Recovered</strong></div>
    <div class="abs benefit" style="left:44px;top:63px">Free Consultation and No Fee<br>Unless <strong>We Recover Money!</strong></div>

    <h2 class="abs bio-title">ACCIDENT<br>LAWYER WALTER<br>GIMSBY, ESQ</h2>
    <p class="abs bio-text">When you have been injured as a result of someone else’s negligence, you may be entitled to compensation. You may be entitled to receive damages in the form of lost wages, pain and suffering and out of pocket costs and expenses for past and future medical treatment. Thousands of clients have entrusted my law firm with the great responsibility of representing their interests. We have recovered millions of dollars for our personal injury clients over the years and we can do the same for you. If you are seeking a New Jersey Personal Injury Lawyer or New York Accident Lawyer you need to feel comfortable with the person in charge of your case. We pride ourselves in our communication with and accessibility to our clients. Any time of day or night we are available to answer your questions. We know injury victims have many concerns after such an unfortunate event; navigating the legal word seeking a way to hold those at fault accountable for the harm they’ve done should not be one of those concerns. Leave that complex work to us!</p>

    <div class="abs brand-name" style="left:414px;top:82px;width:110px">Law Office of<br>Walter Gimsby</div>
    <div class="abs stamp-box" aria-label="stamp area"></div>

    <div class="abs call-label" style="left:151px;top:446px">Call or Text</div>
    <div class="abs call-number" style="left:151px;top:464px">(555) 418-3062</div>
    <div class="abs hours" style="left:329px;top:461px">Available 24 hours<br>a day 7 days per week</div>
  </section>

</div>
</body>
</html>
```